Flyer-Design für  Gassi Service und Hundebetreuung
Flyer-Design für Gassi Service und Hundebetreuung
Zielgruppe
Ich bin biete professionellen Gassi Service und Hundebetreuung, die vor allem auf die Bedürfnisse des Hundes ausgerichtet ist. Meine Zoelgruppe sind Menschen, die ihren Hund als Familienmitglied sehen und denen die Emotionen und Gewaltfreies Arbeiten mit dem Hund wichtig ist.
Aufgabenstellung
Da das Unternehmen neu und noch unbekannt ist soll der Flyer vor allem darauf abzielen Neukunden zu überzeugen und Pfotenfreunde vorstellen. Der Flyer soll in Geschäften oder bei Tierärzten, Futterläden etc. aushängen oder ausliegen. Bei Pfotenfreunde trifft Leidenschaft und liebe für Hunde auf Fachkompetenz zu Hundetraining. Erkennen von Bedürfnissen, Wertschätzung einander, Respekt für einander spielen hier eine Rolle, Fachwissen über Körpersprache beim Hund positiven Training sind die Besonderheiten.
Für die Wiedererkennung soll es zu Website und Logo passen.
Als Schriftarten in Logo oder Briefpapier sind Ciscopic und Poppins genutzt.
Wenn weitere Bilder oder andere Formate vom Logo benötigt werden, bitte melden.

```html
<!DOCTYPE html>
<html lang="de">
<head>
<meta charset="utf-8">
<title>Pfotenfreunde – Gassi-Service und Hundebetreuung</title>
<link href="https://fonts.googleapis.com/css2?family=Amatic+SC:wght@700&family=Poppins:wght@300;400;700&display=swap" rel="stylesheet">
<style>
  :root {
    --green: #93b041;
    --slate: #4b5a63;
    --white: #ffffff;
    --text-font: "Poppins", sans-serif;
    --display-font: "Amatic SC", cursive;
  }
  html, body {
    margin: 0;
    padding: 0;
    overflow: hidden;
    background: #ffffff;
  }
  .flyer {
    position: relative;
    width: 846px;
    height: 1200px;
    overflow: hidden;
    background: var(--green);
    font-family: var(--text-font);
    color: var(--white);
  }
  .flyer-shapes {
    position: absolute;
    inset: 0;
  }
  .contact {
    position: absolute;
    top: 42px;
    right: 75px;
    text-align: right;
    color: var(--slate);
  }
  .contact-label {
    margin: 0;
    font-size: 13.5px;
    font-weight: 400;
    line-height: 1.2;
  }
  .contact-value {
    margin: 0 0 14px;
    font-size: 18.5px;
    font-weight: 700;
    line-height: 1.3;
  }
  .brand-ribbon {
    position: absolute;
    left: 0;
    top: 465px;
    width: 332px;
    height: 161px;
  }
  .brand-name {
    position: absolute;
    left: 0;
    top: 465px;
    width: 290px;
    height: 161px;
    display: flex;
    align-items: center;
    justify-content: center;
    gap: 10px;
    color: var(--slate);
    font-size: 27px;
    font-weight: 700;
  }
  .brand-dot {
    width: 14px;
    height: 14px;
    border-radius: 50%;
    background: var(--green);
  }
  .owner {
    position: absolute;
    left: 70px;
    top: 716px;
    margin: 0;
    font-size: 24px;
    font-weight: 400;
    letter-spacing: 1px;
  }
  .headline {
    position: absolute;
    left: 68px;
    top: 744px;
    margin: 0;
    font-family: var(--display-font);
    font-weight: 700;
    font-size: 86px;
    line-height: 72px;
    letter-spacing: 1px;
  }
  .column {
    position: absolute;
    top: 945px;
  }
  .column-left { left: 65px; width: 330px; }
  .column-right { left: 440px; width: 340px; }
  .subline {
    display: inline-block;
    margin: 0;
    padding: 0 10px;
    height: 42px;
    line-height: 44px;
    background: var(--white);
    color: var(--green);
    font-family: var(--display-font);
    font-weight: 700;
    font-size: 38px;
  }
  .column-text {
    margin: 20px 0 0 8px;
    font-size: 15px;
    font-weight: 400;
    line-height: 19.4px;
  }
  .column-left .column-text { text-align: justify; hyphens: manual; }
  .bullet-list {
    list-style: none;
    margin: 22px 0 0 8px;
    padding: 0;
    font-size: 15.5px;
    line-height: 25px;
  }
  .bullet-list li::before {
    content: "• ";
  }
</style>
</head>
<body>
<main class="flyer">
  <svg class="flyer-shapes" width="846" height="1200" viewBox="0 0 846 1200" aria-hidden="false">
    <defs>
      <linearGradient id="photo-base" x1="0" y1="0" x2="1" y2="1">
        <stop offset="0" stop-color="#c7b98a"/>
        <stop offset="0.25" stop-color="#ece6dc"/>
        <stop offset="0.5" stop-color="#c8703f"/>
        <stop offset="0.8" stop-color="#9a4a26"/>
        <stop offset="1" stop-color="#c9853a"/>
      </linearGradient>
      <radialGradient id="photo-light" cx="0.72" cy="0.62" r="0.35">
        <stop offset="0" stop-color="#f4f1ec" stop-opacity="0.85"/>
        <stop offset="0.6" stop-color="#8a5a44" stop-opacity="0.5"/>
        <stop offset="1" stop-color="#8a5a44" stop-opacity="0"/>
      </radialGradient>
    </defs>
    <g role="img" aria-label="Foto: Australian Shepherd in braun-weiß sitzt vor herbstlicher, unscharfer Landschaft">
      <path d="M0 0 H528 C545 90 600 150 680 170 C760 190 810 210 846 245 V780 C740 790 640 730 540 650 C440 570 330 470 240 420 C160 380 70 370 0 374 Z" fill="url(#photo-base)"/>
      <path d="M0 0 H528 C545 90 600 150 680 170 C760 190 810 210 846 245 V780 C740 790 640 730 540 650 C440 570 330 470 240 420 C160 380 70 370 0 374 Z" fill="url(#photo-light)"/>
    </g>
    <polygon class="brand-ribbon-shape" points="0,465 332,465 287,546 332,626 0,626" fill="#ffffff"/>
    <g fill="#4b5a63" role="img" aria-label="Pfotenabdrücke als Dekoration">
      <circle cx="755" cy="757" r="20"/>
      <circle cx="728" cy="862" r="20"/>
      <circle cx="832" cy="917" r="20"/>
      <circle cx="808" cy="1062" r="20"/>
      <circle cx="728" cy="1160" r="20"/>
    </g>
  </svg>

  <section class="contact">
    <p class="contact-label">Erfahren Sie mehr unter</p>
    <p class="contact-value">pfotenfreunde.de</p>
    <p class="contact-label">unter rufen Sie mich an:</p>
    <p class="contact-value">0123 456 78 90</p>
  </section>

  <div class="brand-name"><span class="brand-dot"></span>Pfotenfreunde</div>

  <p class="owner">MARA MUSTERFRAU</p>
  <h1 class="headline">Gassi-Service<br>und Hundebetreuung</h1>

  <section class="column column-left">
    <h2 class="subline">Subline 1</h2>
    <p class="column-text">Con ni ut quas sandandae voluptur sum voluptatis aut qui rerferum de nectibus, cone abo. Ut quiae pro magnisquo ipit exceat expeliquam, occusam quam vo-luptatur aut arum alis por ad min rem qui rerferum de nectibus, cone abo. Ut esto dollor magnis eos esciis.</p>
  </section>

  <section class="column column-right">
    <h2 class="subline">Subline 2</h2>
    <p class="column-text">Con ni ut quas sandandae voluptur sum voluptatis aut quiae pro. Et quiae pro :</p>
    <ul class="bullet-list">
      <li>Stichpunkt</li>
      <li>Stichpunkt</li>
      <li>Stichpunkt</li>
    </ul>
  </section>
</main>
</body>
</html>
```